Natural deodorant label

Natural clean deodorant line. Need modernize label which can be sized for both the regular and travel size deodorants. 2.75 x 3" and 1x2". Important to highlight no baking soda and its natural. Also has no aluminum, preservatives, nor chemicals. Its gender inclusive and safe for all ages. Please see website at www.lorvatique.com. will attach current label. Will need a label that i would be able to update with new scents as they come. Want a clean look.
Updates

Need extra days to review

Target Market(s)

the working mother/wife that lives a clean healthy life and pushes that for her family

Industry/Entity Type

health and beauty/deodorant/natural

Colors

Designer to choose colors to be used in the design.

Requirements
Must have
• No baking soda and gender inclusive on label. Clean look. Very little to no picture art.
Nice to have
• Potentially a different color representing the different scents. A brief description of the deodorant scent underneath the scent name. This can be found under the drop down menu titled valdora deodorant scents on the website www.lorvatique.com. Area on front label for a small barcode.
Should not have
• misspelled words; dark label

```html
<!DOCTYPE html>
<html lang="en">
<head>
<meta charset="utf-8">
<title>Lorvatique Valdora Deodorant Label</title>
<link rel="stylesheet" href="https://fonts.googleapis.com/css2?family=Arvo:wght@700&family=Crimson+Text:wght@400&family=Josefin+Sans:wght@300&display=swap">
<style>
  :root {
    --page-bg: #f1f1f1;
    --label-bg: #eceeed;
    --frame-brown: #7c6b5d;
    --text-brown: #7a6c61;
    --badge-brown: #7c6b5d;
    --badge-gold: #d8c97f;
    --badge-gold-text: #ffffff;
    --leaf-light: #b9d59a;
    --leaf-dark: #6f9a45;
  }
  * { margin: 0; padding: 0; box-sizing: border-box; }
  html, body {
    width: 1200px;
    height: 1000px;
    overflow: hidden;
    background: var(--page-bg);
  }
  .canvas {
    position: relative;
    width: 1200px;
    height: 1000px;
  }
  .label {
    position: absolute;
    left: 340px;
    top: 60px;
    width: 520px;
    height: 880px;
    background: var(--label-bg);
  }
  .label-frame {
    position: absolute;
    inset: 0;
    border: 7px solid var(--frame-brown);
  }
  .brand {
    position: absolute;
    top: 66px;
    left: 0;
    width: 100%;
    display: flex;
    flex-direction: column;
    align-items: center;
  }
  .brand-dot {
    width: 62px;
    height: 62px;
    border-radius: 50%;
    background: var(--text-brown);
  }
  .brand-name {
    margin-top: 22px;
    font-family: "Crimson Text", serif;
    font-size: 38px;
    font-weight: 400;
    color: var(--text-brown);
    letter-spacing: 1px;
    line-height: 1;
  }
  .product-name {
    position: absolute;
    top: 280px;
    width: 100%;
    text-align: center;
    font-family: "Josefin Sans", sans-serif;
    font-weight: 300;
    font-size: 88px;
    color: var(--text-brown);
    letter-spacing: 1px;
    line-height: 1;
  }
  .scent-name {
    position: absolute;
    top: 425px;
    width: 100%;
    text-align: center;
    font-family: "Arvo", serif;
    font-weight: 700;
    font-size: 26px;
    color: var(--text-brown);
    letter-spacing: 0.5px;
  }
  .badge {
    position: absolute;
    left: 13px;
    font-family: "Arvo", serif;
    font-weight: 700;
    font-size: 17px;
    line-height: 1.15;
    text-transform: uppercase;
    padding: 14px 16px;
    color: #ffffff;
  }
  .badge-gender {
    top: 547px;
    width: 152px;
    height: 80px;
    background: var(--badge-brown);
  }
  .badge-soda {
    top: 650px;
    width: 110px;
    height: 82px;
    background: var(--badge-gold);
    color: var(--badge-gold-text);
    font-size: 15px;
    padding: 10px 12px;
  }
  .claims {
    position: absolute;
    top: 770px;
    width: 100%;
    text-align: center;
    font-family: "Crimson Text", serif;
    font-size: 28px;
    line-height: 1.3;
    color: var(--text-brown);
  }
  .leaf-art {
    position: absolute;
    border-radius: 40% 60% 50% 50%;
    background: linear-gradient(150deg, var(--leaf-light), var(--leaf-dark));
    opacity: 0.85;
  }
  .leaf-art-top {
    left: -48px;
    top: 27px;
    width: 141px;
    height: 227px;
  }
  .leaf-art-bottom {
    left: 427px;
    top: 494px;
    width: 152px;
    height: 227px;
  }
</style>
</head>
<body>
  <div class="canvas">
    <div class="label">
      <div class="label-frame"></div>
      <div class="leaf-art leaf-art-top" role="img" aria-label="Watercolour green vine with leaves trailing over the top left corner"></div>
      <div class="leaf-art leaf-art-bottom" role="img" aria-label="Watercolour green vine with leaves at the lower right edge"></div>

      <div class="brand">
        <div class="brand-dot"></div>
        <div class="brand-name">Lorvatique</div>
      </div>

      <h1 class="product-name">VALDORA</h1>
      <p class="scent-name">ISLAND BREEZE</p>

      <div class="badge badge-gender">Gender<br>Inclusive</div>
      <div class="badge badge-soda">No<br>Baking<br>Soda</div>

      <p class="claims">NATURALLY REFRESHING<br>NET WT 2.5 OZ (70G)</p>
    </div>
  </div>
</body>
</html>
```